Wedding Company needs Brochure Design

FOR THIS PROJECT, WE ARE LOOKING FOR A BROCHURE. WHOEVER WE CHOOSE AS THE WINNING BROCHURE DESIGN WILL THEN DESIGN OUR WEBSITE AND BUSINESS CARD.

We're are looking to expand our brochure by making it a circle and adding 6 inside pages of information with a front and back cover. The pages will be as follows:

Front
About us
About us pictures
Wedding Planning
Wedding planning pictures
Lighting & Decor
Lighting & decor pictures
Back

We've uploaded a picture of our current brochure... so you can get an idea of what we've liked before. Please give us your creative input & design ideas. We've put together a "mock" brochure for you to take a look at as well. As you can see we need your help to properly lay out pictures so that the pages look full and the pictures pop and catches our clients attention.

A few words to describe our brochure would be "elegance", "class", "tasteful" and "colorful". We want to be able to portray that we are luxurious and innovative for the higher end brides and at the same time catering to the budget friendly brides.

Currently, we are waiting on a few pictures from the photographers and we are hoping to have them in a few days... In the meantime we've placed pictures we took from our phone as place holders.

Industry/Entity Type

Catering

```html
<!DOCTYPE html>
<html lang="en">
<head>
<meta charset="utf-8">
<title>Wedding Planning and Coordination — Brochure Spread</title>
<link href="https://fonts.googleapis.com/css2?family=Allura&family=Italianno&family=Parisienne&display=swap" rel="stylesheet">
<style>
  :root {
    --page-bg: #ffffff;
    --panel-light: #e5e5e6;
    --panel-dark: #7f8083;
    --ink: #2b2b2b;
    --accent-purple: #7a3f8f;
    --card-white: #ffffff;
    --card-shadow: rgba(0,0,0,0.18);
    --rule-dots: #9a9a9a;
  }
  html, body {
    margin: 0;
    padding: 0;
    width: 1200px;
    height: 668px;
    overflow: hidden;
    background: var(--page-bg);
  }
  .spread {
    position: relative;
    width: 1200px;
    height: 668px;
    overflow: hidden;
    font-family: "Allura", cursive;
    color: var(--ink);
  }
  .panel-left {
    position: absolute;
    left: -26px;
    top: -6px;
    width: 680px;
    height: 680px;
    border-radius: 50%;
    background: var(--panel-light);
  }
  .photo-circle {
    position: absolute;
    left: 0;
    top: 0;
  }
  .polaroid-stack {
    position: absolute;
    left: 170px;
    top: 40px;
    width: 330px;
    height: 300px;
  }
  .polaroid {
    position: absolute;
    background: var(--card-white);
    box-shadow: 0 1px 4px var(--card-shadow);
    border: 1px solid #cfcfcf;
  }
  .polaroid--back-1 { left: 4px; top: 12px; width: 300px; height: 258px; transform: rotate(-2deg); }
  .polaroid--back-2 { left: 16px; top: 6px; width: 300px; height: 258px; transform: rotate(2.5deg); }
  .polaroid--front {
    left: 10px; top: 22px; width: 310px; height: 262px;
  }
  .polaroid__photo {
    position: absolute;
    left: 10px;
    top: 8px;
    width: 290px;
    height: 192px;
    background: radial-gradient(ellipse at 50% 30%, #7a4fa8 0%, #3b2350 45%, #141018 100%);
  }
  .polaroid__caption {
    position: absolute;
    left: 0;
    right: 0;
    top: 214px;
    text-align: center;
    white-space: nowrap;
    font-family: "Parisienne", cursive;
    font-size: 17px;
    line-height: 24px;
    color: var(--accent-purple);
  }
  .intro {
    position: absolute;
    left: 28px;
    top: 341px;
    width: 556px;
    margin: 0;
    text-align: center;
    font-family: "Italianno", cursive;
    font-size: 19px;
    line-height: 23.5px;
  }
  .services-heading {
    position: absolute;
    left: 75px;
    top: 462px;
    width: 500px;
    display: flex;
    align-items: center;
    gap: 6px;
    font-size: 19px;
    white-space: nowrap;
  }
  .services-heading::before,
  .services-heading::after {
    content: "";
    flex: 1;
    border-top: 1px dotted var(--rule-dots);
  }
  .service {
    position: absolute;
    font-size: 18px;
    white-space: nowrap;
  }
</style>
</head>
<body>
<div class="spread">
  <div class="panel-left"></div>

  <svg class="photo-circle" width="1200" height="668" viewBox="0 0 1200 668">
    <defs>
      <clipPath id="gallery-clip">
        <circle cx="902" cy="334" r="291"/>
      </clipPath>
      <linearGradient id="g-dance" x1="0" y1="0" x2="0" y2="1">
        <stop offset="0" stop-color="#5b4a8a"/><stop offset="0.6" stop-color="#8c7bb8"/><stop offset="1" stop-color="#d9d2e6"/>
      </linearGradient>
      <linearGradient id="g-field" x1="0" y1="0" x2="0" y2="1">
        <stop offset="0" stop-color="#e8ecef"/><stop offset="0.5" stop-color="#c4b8a8"/><stop offset="1" stop-color="#8c7a66"/>
      </linearGradient>
      <linearGradient id="g-hall" x1="0" y1="0" x2="0" y2="1">
        <stop offset="0" stop-color="#2f6f78"/><stop offset="0.5" stop-color="#3b3a3a"/><stop offset="1" stop-color="#8a7a66"/>
      </linearGradient>
      <linearGradient id="g-reception" x1="0" y1="0" x2="0" y2="1">
        <stop offset="0" stop-color="#a04aa8"/><stop offset="0.5" stop-color="#3fa6d6"/><stop offset="1" stop-color="#2a2740"/>
      </linearGradient>
      <linearGradient id="g-garden" x1="0" y1="0" x2="0" y2="1">
        <stop offset="0" stop-color="#6f8a4a"/><stop offset="0.6" stop-color="#3a4a2c"/><stop offset="1" stop-color="#d8d8d0"/>
      </linearGradient>
      <linearGradient id="g-drape" x1="0" y1="0" x2="0" y2="1">
        <stop offset="0" stop-color="#f3ece2"/><stop offset="0.6" stop-color="#d8b88a"/><stop offset="1" stop-color="#6a5a48"/>
      </linearGradient>
      <radialGradient id="g-flowers" cx="0.5" cy="0.5" r="0.7">
        <stop offset="0" stop-color="#e6a6d0"/><stop offset="0.6" stop-color="#9a4ab0"/><stop offset="1" stop-color="#4a6a3a"/>
      </radialGradient>
    </defs>
    <circle class="gallery-ring" cx="902" cy="334" r="304" fill="var(--panel-dark)"/>
    <g clip-path="url(#gallery-clip)">
      <rect x="600" y="30" width="600" height="620" fill="var(--panel-dark)"/>
      <rect x="618" y="30" width="182" height="300" fill="url(#g-dance)" role="img" aria-label="Photo: couple sharing a first dance under string lights"/>
      <rect x="618" y="340" width="182" height="310" fill="url(#g-garden)" role="img" aria-label="Photo: grooms walking down a garden aisle"/>
      <rect x="808" y="20" width="184" height="168" fill="url(#g-field)" role="img" aria-label="Photo: couple embracing in an open field with bouquet in front"/>
      <rect x="808" y="197" width="184" height="275" fill="url(#g-reception)" role="img" aria-label="Photo: reception hall with purple and blue uplighting and centerpieces"/>
      <rect x="808" y="482" width="184" height="168" fill="url(#g-drape)" role="img" aria-label="Photo: ballroom with white ceiling draping and warm lighting"/>
      <rect x="1002" y="40" width="180" height="290" fill="url(#g-hall)" role="img" aria-label="Photo: arched hall set with ceremony chairs and chandeliers"/>
      <rect x="1002" y="340" width="180" height="300" fill="url(#g-flowers)" role="img" aria-label="Photo: close-up of purple and pink floral arrangement"/>
    </g>
  </svg>

  <div class="polaroid-stack">
    <div class="polaroid polaroid--back-1"></div>
    <div class="polaroid polaroid--back-2"></div>
    <div class="polaroid polaroid--front">
      <div class="polaroid__photo" role="img" aria-label="Photo: wedding team group portrait on a purple-lit stage"></div>
      <div class="polaroid__caption">Wedding Planning and Coordination</div>
    </div>
  </div>

  <p class="intro">With all success and joy we have experienced in providing our expertise and quality service, we are now prepared to include the planning and execution of your entire wedding. We've partnered together with top notch vendors in the Southern California area to put together a phenomenal wedding full of unforgettable memories for both the happy couple and their guests. We are your one stop shop for all things weddings!</p>

  <div class="services-heading">We can assist you in finding the following:</div>

  <span class="service" style="left:106px; top:512px;">- Caterer</span>
  <span class="service" style="left:200px; top:512px;">- Florist</span>
  <span class="service" style="left:304px; top:512px;">- Photographer</span>
  <span class="service" style="left:428px; top:512px;">- Dj or Band Services</span>
  <span class="service" style="left:142px; top:544px;">- Bartending Services</span>
  <span class="service" style="left:304px; top:544px;">- Cake</span>
  <span class="service" style="left:416px; top:544px;">- Rentals/ Linens</span>
  <span class="service" style="left:180px; top:574px;">- Decor Items</span>
  <span class="service" style="left:316px; top:576px;">- Planning and Coordination</span>
</div>
</body>
</html>
```